Word Press Website Design with animated splash page + Coding

Web Site Brief
Domain: www.mervalink.ai
Job:
Word Press Site creative and coding, we have word press hosting through HostPrairie and will grant access to the winning design to implement the site.
Splash page with animation of our current logo.
Approx 7 pages (several are the same layout)
We require the ability to add/update text and pictures to the site ourselves after initial build.
All pages other than splash should have a floating button as a way to connect with us and open to a simple form that allows for contact information and then sends to an email we select.
Background:
After a year of R&D TRB is launching our new ai driven product to market. As such we are also rebranding from www.trbpartners.com to www.mervalink.ai. Our customers are large technology companies and TRB has been in business for the last 20 years.
Site Overview:
We are looking for a fairly simple site with regards to pages but one that brings a look and feel of high tech and new. We are not tied to the more standard website design as we are looking forward not to the past or even today. The initial content will be fairly simple and straight forward mainly made up of pictures with text. Although the content will be fairly simple to start we want some wow factor for the layout and functionality.
Site Specifics:
We recently had a new logo designed and have all color and file type versions available. We have posted a zipped filed with all the PNG files in different colors layouts. We will require a link to our social media LinkedIn, FaceBook, Twitter.
We are including a power point with a basic layout of our site as follows:
Site Layout:
Splash Page:
This will be the first page reached and we would like the "Market Lenses" part of our logo there then animate the first part of our logo. For the animation you can go to this site www.quenvestry.com and see how the red circle builds. Starting with the C then the S and last the G. At the same time we would like the following phrase to build under our logo “Ai Driven Business Insight and Revenue Generation Solutions”. The build should take somewhere around 4 seconds then move to our main page.
Main Page:
The main page will contain 5 links to the next layer of pages.
Layer 1 page type 1: (3 of the 5 pages)
Page type one will have some overall text at the top then we are looking for a two column table with text and then a standardized picture size format. As we will have different size picture to include we would like to keep the grid/table standardized with the same picture size (similar to a thumb nail but not that small) that can then pop out to full size when you hover or click.
Layer 1 page type 2: (2 of the 5 pages)
These two pages will mainly be text but the layout is not yet determined.
We are also including a powerpoint deck with more information on each of the 5 subpages. Most contain pictures you can use for the layout design of the 3 subpages that have pictures embedded.
We will be judging look and feel for the splash page, the main page, and the two types of sub pages. Once we select the winner credentials will be granted to use your design to build out the page in Wordpress on our current hosting site.
We would like to find a designer we can continue to work with as we develop the site further.
thanks

```html
<!DOCTYPE html>
<html lang="en">
<head>
<meta charset="utf-8">
<title>Mervalink – TRB Services</title>
<link href="https://fonts.googleapis.com/css2?family=Bebas+Neue&family=Questrial&family=Open+Sans:wght@400;600;700&display=swap" rel="stylesheet">
<style>
:root{
  --blue:#1ab2e8;
  --ink:#263545;
  --yellow:#fcc400;
  --pale-yellow:#f5e6ab;
  --pale-blue:#d5e9f2;
  --page:#f2f2f2;
  --white:#ffffff;
  --grey-text:#6f6f6f;
  --button-dark:#3b3b3b;
  --clients-band:#a9b0b9;
  --footer:#d6d6d6;
  --bottom-bar:#263444;
}
*{margin:0;padding:0;box-sizing:border-box}
html,body{width:1200px;height:4996px;overflow:hidden}
body{font-family:'Questrial',sans-serif;color:var(--ink);background:var(--page);position:relative}
.display{font-family:'Bebas Neue',sans-serif;font-weight:400;letter-spacing:0.5px;line-height:1}
section,header,footer{position:absolute;left:0;width:1200px}
.abs{position:absolute}

/* header */
.site-header{top:0;height:74px;background:var(--white);box-shadow:0 1px 3px rgba(0,0,0,.06);z-index:5}
.brand{position:absolute;display:flex;align-items:center;gap:8px;color:var(--blue);font-size:22px;letter-spacing:1px}
.brand-dot{width:30px;height:30px;border-radius:50%;border:4px solid var(--blue)}
.site-header .brand{left:93px;top:21px}
.main-nav{position:absolute;top:30px;left:584px;font-size:13px;color:#6a6a6a}
.main-nav a{position:absolute;white-space:nowrap;text-decoration:none;color:inherit}
.main-nav .active{color:var(--blue);border-bottom:2px solid var(--blue);padding-bottom:6px}
.social-top{position:absolute;top:27px;left:983px;display:flex;gap:20px}
.social-top span{width:17px;height:17px;background:#111;border-radius:3px}

/* hero */
.hero{top:74px;height:580px;background:linear-gradient(90deg,#f1f2f4 0%,#e9ebee 60%,#dfe2e6 100%)}
.hero-photo{position:absolute;left:640px;top:0;width:560px;height:518px;background:radial-gradient(ellipse at 55% 45%,#b7bcc4 0%,#d5d8dd 55%,rgba(223,226,230,0) 80%)}
.hero-kicker{position:absolute;left:186px;top:124px;font-size:28px;color:var(--ink)}
.hero-title{position:absolute;left:186px;top:172px;font-size:62px}
.hero-title .blue{color:var(--blue);display:block}
.hero-title .dark{display:block;margin-top:4px}
.hero-sub{position:absolute;left:186px;top:312px;font-size:25px}
.btn-blue{display:inline-block;background:var(--blue);color:var(--ink);border-radius:6px;font-size:14px;text-align:center}
.hero .btn-blue{position:absolute;left:186px;top:362px;width:136px;height:35px;line-height:35px}

/* services */
.services{top:654px;height:1512px;background:var(--page);overflow:hidden}
.services-title{position:absolute;left:186px;top:115px;font-size:60px;color:var(--blue)}
.services-lead{position:absolute;left:186px;top:196px;width:560px;font-size:24px;line-height:30px}
.services-body{position:absolute;left:186px;top:318px;width:325px;font-size:14.5px;line-height:18.5px}
.service-card{position:absolute;width:252px;height:519px;background:var(--white);border-radius:8px;box-shadow:0 4px 14px rgba(0,0,0,.16);overflow:hidden;text-align:center}
.card-media{height:311px}
.card-title{font-size:23px;margin-top:34px;color:#222}
.card-text{font-size:13.5px;line-height:14px;width:210px;margin:14px auto 0;color:#222}
.service-card .btn-blue{width:136px;height:35px;line-height:35px;margin-top:18px}

/* about */
.about{top:2166px;height:576px;background:var(--yellow)}
.about-photo{position:absolute;left:0;top:0;width:485px;height:576px;background:radial-gradient(ellipse at 45% 55%,#1f5f73 0%,#c89a4a 45%,#f7b800 78%)}
.about-title{position:absolute;left:531px;top:84px;font-size:60px}
.about-text{position:absolute;left:531px;top:183px;width:480px;font-size:25px;line-height:30px}
.about-text p+p{margin-top:30px}

/* featured */
.featured{top:2742px;height:576px;background:#fafafa;text-align:center}
.featured-title{position:absolute;left:0;width:1200px;top:62px;font-size:60px}
.featured-rule{position:absolute;left:561px;top:130px;width:78px;height:2px;background:#ccc}
.solution{position:absolute;top:200px;width:300px;margin-left:-150px}
.solution-icon{width:50px;height:50px;border-radius:50%;background:#3a3a3a;margin:0 auto;display:flex;align-items:center;justify-content:center}
.solution h3{font-family:'Open Sans',sans-serif;font-weight:600;font-size:21px;margin-top:28px;color:#333}
.solution p{font-family:'Open Sans',sans-serif;font-size:9.5px;line-height:17px;color:var(--grey-text);margin-top:14px;padding:0 4px}
.btn-dark{display:inline-block;width:126px;height:42px;line-height:42px;background:var(--button-dark);color:#fff;font-family:'Open Sans',sans-serif;font-size:13px;margin-top:84px}

/* testimonials */
.testimonials{top:3318px;height:1000px;background:var(--page);overflow:hidden}
.testimonials-title{position:absolute;right:95px;top:120px;font-size:62px;text-align:right}
.testimonials-sub{position:absolute;right:95px;top:190px;font-size:25px;line-height:31px;text-align:right}
.avatar{position:absolute;border-radius:50%;border:3px solid var(--white);box-shadow:0 3px 8px rgba(0,0,0,.18)}
.quote-text{position:absolute;left:190px;top:528px;width:480px;text-align:center;font-size:16px;line-height:19px}

/* clients */
.clients{top:4318px;height:312px;background:var(--clients-band);border-top:1px solid #8e969f;border-bottom:1px solid #8e969f}
.clients-title{position:absolute;left:0;width:1200px;top:52px;text-align:center;font-size:60px}
.client{position:absolute;top:190px;transform:translateX(-50%);display:flex;align-items:center;gap:7px;color:var(--white);font-size:18px}
.client i{width:16px;height:16px;border-radius:50%;background:var(--white)}

/* footer */
.site-footer{top:4630px;height:312px;background:var(--footer)}
.site-footer .brand{left:93px;top:82px;font-size:36px;color:#233442;gap:10px}
.site-footer .brand-dot{width:52px;height:52px;border-width:6px;border-color:#233442}
.footer-blurb{position:absolute;left:93px;top:140px;width:215px;font-size:9.5px;line-height:13px;color:#7a7a7a}
.footer-social{position:absolute;left:98px;top:206px;display:flex;gap:24px}
.footer-social span{width:14px;height:14px;border:1.5px solid #555;border-radius:50%}
.footer-col{position:absolute;top:88px;font-size:14px;color:#233442}
.footer-col h4{font-weight:600;font-family:'Open Sans',sans-serif;font-size:14px;margin-bottom:14px}
.footer-col li{list-style:none;font-size:11px;color:#555;line-height:30px}
.bottom-bar{position:absolute;top:4942px;left:0;width:1200px;height:54px;background:var(--bottom-bar);color:var(--white);font-family:'Open Sans',sans-serif;font-size:8px;font-weight:600}
.bottom-bar span{position:absolute;top:22px}
</style>
</head>
<body>

<header class="site-header">
  <div class="brand"><span class="brand-dot"></span>MERVALINK</div>
  <nav class="main-nav">
    <a class="active" style="left:0">Home</a>
    <a style="left:85px">Services</a>
    <a style="left:165px">About</a>
    <a style="left:232px">Blog</a>
    <a style="left:292px">Contact</a>
  </nav>
  <div class="social-top" role="img" aria-label="Social media links">
    <span></span><span></span><span></span><span></span>
  </div>
</header>

<section class="hero">
  <div class="hero-photo" role="img" aria-label="Business team in suits leaping through the air"></div>
  <p class="hero-kicker display">TRB Services helps increase your</p>
  <h1 class="hero-title display"><span class="blue">Business Plans</span><span class="dark">Overall Effectiveness</span></h1>
  <p class="hero-sub">Integrating all your strategies in one place.</p>
  <a class="btn-blue">Contact Us</a>
</section>

<section class="services">
  <svg class="abs" style="left:0;top:0" width="1200" height="1512" aria-hidden="true">
    <polygon points="0,40 417,676 0,676" fill="var(--pale-yellow)"/>
    <path d="M1010,300 C1120,240 1200,280 1200,330 L1200,1230 C1120,1280 1000,1270 880,1180 C790,1100 790,960 830,830 C870,690 900,380 1010,300 Z" fill="var(--pale-blue)"/>
  </svg>
  <h2 class="services-title display">Our Services</h2>
  <p class="services-lead">TRB Services is an all encompassing Sales and Marketing firm, which means we have 360 solutions.</p>
  <p class="services-body">As your one stop shop for channel, sales and marketing, we can develop strategy and manage a fully outsourced campaign, or provide a la carte services to plug into a campaign already in flight and everything in between! We can work seamlessly with existing teams to create an efficient engine to drive your initiatives forward.</p>

  <article class="service-card" style="left:855px;top:19px">
    <div class="card-media" role="img" aria-label="Glowing digital growth chart graphic" style="background:radial-gradient(circle at 50% 40%,#7fd0f0,#2a59b8 55%,#1b2a6a)"></div>
    <h3 class="card-title display">SDR Velocity</h3>
    <p class="card-text">Aliquam faucibus, odio nec commodo aliquam, neque felis placerat dui, a porta ante</p>
    <a class="btn-blue">Know More</a>
  </article>
  <article class="service-card" style="left:556px;top:310px">
    <div class="card-media" role="img" aria-label="Hand tapping a screen with floating chat icons" style="background:linear-gradient(160deg,#1d2f52,#6f86a8 55%,#c9d3df)"></div>
    <h3 class="card-title display">Sales Organizations</h3>
    <p class="card-text">Integer ac interdum lacus. Nunc porta semper lacus a varius. Pellentesque habitant</p>
    <a class="btn-blue">Know More</a>
  </article>
  <article class="service-card" style="left:855px;top:593px">
    <div class="card-media" role="img" aria-label="Man in glasses overlaid with digital world graphics" style="background:linear-gradient(120deg,#0d1f33,#2a6a99 60%,#b7dff2)"></div>
    <h3 class="card-title display">TRB Sales Intelligence</h3>
    <p class="card-text">Vestibulum blandit viverra convallis. Pellentesque ligula urna, fermentum ut semper in,</p>
    <a class="btn-blue">Know More</a>
  </article>
  <article class="service-card" style="left:256px;top:690px">
    <div class="card-media" role="img" aria-label="Laptop showing marketing charts on a desk" style="background:linear-gradient(170deg,#4a4f57,#9aa0a8 50%,#e3e5e8)"></div>
    <h3 class="card-title display">Marketing Organizations</h3>
    <p class="card-text">Duis mauris augue, efficitur eu arcu sit amet, posuere dignissim neque. Aenean enim</p>
    <a class="btn-blue">Know More</a>
  </article>
  <article class="service-card" style="left:556px;top:886px">
    <div class="card-media" role="img" aria-label="Hands at a laptop with data icons overlaid" style="background:linear-gradient(160deg,#8a5a3c,#d9b79b 50%,#f1e7dd)"></div>
    <h3 class="card-title display">Sales Intelligence</h3>
    <p class="card-text">Aenean sed lorem est. Sed quis neque ut nibh suscipit imperdiet ac non augue.</p>
    <a class="btn-blue">Know More</a>
  </article>
</section>

<section class="about">
  <div class="about-photo" role="img" aria-label="Smiling woman with red hair making a heart shape with her hands"></div>
  <h2 class="about-title display">About Us</h2>
  <div class="about-text">
    <p>We are a fast paced, agile organization that prides itself on helping our b2b clients solve business challenges by providing prescriptive solutions efficiently and in an on-demand, turnkey manner.</p>
    <p>We solve the challenges many organizations face by offering the appropriate channel, marketing, sales, or resource solution.</p>
  </div>
</section>

<section class="featured">
  <h2 class="featured-title display">Featured Solutions</h2>
  <div class="featured-rule"></div>
  <div class="solution" style="left:275px">
    <div class="solution-icon"><svg width="20" height="20" viewBox="0 0 20 20" fill="none" stroke="#fff" stroke-width="1.6"><circle cx="10" cy="4" r="2"/><line x1="10" y1="6" x2="10" y2="17"/><path d="M4 11 Q5 17 10 17 Q15 17 16 11"/><line x1="7" y1="9" x2="13" y2="9"/></svg></div>
    <h3>Solution</h3>
    <p>Lorem ipsum dolor sit amet, consetetur sadipscing elitr, sed diam nonumy eirmod tempor invidunt ut labore et dolore magna.</p>
    <a class="btn-dark">Read More</a>
  </div>
  <div class="solution" style="left:599px">
    <div class="solution-icon"><svg width="20" height="20" viewBox="0 0 20 20" fill="none" stroke="#fff" stroke-width="1.6"><line x1="5" y1="3" x2="5" y2="18"/><path d="M5 4 H15 L13 8 L15 12 H5"/></svg></div>
    <h3>Solution</h3>
    <p>Lorem ipsum dolor sit amet, consetetur sadipscing elitr, sed diam nonumy eirmod tempor invidunt ut labore et dolore magna.</p>
    <a class="btn-dark">Read More</a>
  </div>
  <div class="solution" style="left:923px">
    <div class="solution-icon"><svg width="20" height="20" viewBox="0 0 20 20" fill="none" stroke="#fff" stroke-width="1.6"><circle cx="10" cy="7" r="4.5"/><path d="M7 11 L6 18 L10 16 L14 18 L13 11"/></svg></div>
    <h3>Solution</h3>
    <p>Lorem ipsum dolor sit amet, consetetur sadipscing elitr, sed diam nonumy eirmod tempor invidunt ut labore et dolore magna.</p>
    <a class="btn-dark">Read More</a>
  </div>
</section>

<section class="testimonials">
  <svg class="abs" style="left:0;top:0" width="1200" height="1000" aria-hidden="true">
    <path d="M330,150 C470,70 700,110 790,230 C850,320 800,460 740,600 C690,720 560,800 420,830 C300,860 170,870 130,780 C90,680 95,520 110,380 C125,260 220,210 330,150 Z" fill="var(--pale-blue)"/>
  </svg>
  <h2 class="testimonials-title display">Testimonials</h2>
  <p class="testimonials-sub">Let's see what our clients<br>talk about as</p>
  <div class="avatar" role="img" aria-label="Client portrait" style="left:522px;top:171px;width:108px;height:108px;background:#b98a6e"></div>
  <div class="avatar" role="img" aria-label="Client portrait" style="left:173px;top:254px;width:108px;height:108px;background:#8f949b"></div>
  <div class="avatar" role="img" aria-label="Client portrait" style="left:352px;top:342px;width:152px;height:152px;background:#7a5a4a"></div>
  <div class="avatar" role="img" aria-label="Client portrait" style="left:662px;top:401px;width:108px;height:108px;background:#d8b88e"></div>
  <div class="avatar" role="img" aria-label="Client portrait" style="left:119px;top:642px;width:108px;height:108px;background:#7c6a5e"></div>
  <div class="avatar" role="img" aria-label="Client portrait" style="left:470px;top:661px;width:108px;height:108px;background:#d7c3a8"></div>
  <p class="quote-text">Integer ac interdum lacus. Nunc porta semper lacus a varius. Pellentesque habitant morbi tristique senectus et netus et malesuada fames ac turpis egestas. Nunc sagittis consectetur velit, ac gravida nunc gravida et. Vestibulum at eros imperdiet, volutpat nunc vitae, ornare erat. Proin interdum aliquet porta. Fusce ut semper ligula.</p>
</section>

<section class="clients">
  <h2 class="clients-title display">Meet Our Clients</h2>
  <div class="client" style="left:186px"><i></i>Norvane</div>
  <div class="client" style="left:394px"><i></i>Quillsoft</div>
  <div class="client" style="left:599px"><i></i>Delvar</div>
  <div class="client" style="left:805px"><i></i>Bridgepeak</div>
  <div class="client" style="left:1008px"><i></i>Ostrel</div>
</section>

<footer class="site-footer">
  <div class="brand"><span class="brand-dot"></span>MERVALINK</div>
  <p class="footer-blurb">Mauris neque nisl, faucibus non elementum in, convallis et eros. Sed pretium sem libero, vel pellentesque purus ultrices ut. In quis leo id</p>
  <div class="footer-social" role="img" aria-label="Social media and phone links"><span></span><span></span><span></span><span></span><span></span></div>
  <div class="footer-col" style="left:807px"><h4>Products</h4><ul><li>Product 1</li><li>Product 2</li><li>Product 3</li><li>Product 4</li></ul></div>
  <div class="footer-col" style="left:921px"><h4>Services</h4><ul><li>Service 1</li><li>Service 2</li><li>Service 3</li><li>Service 4</li></ul></div>
  <div class="footer-col" style="left:1035px"><h4>Resources</h4><ul><li>News</li><li>Blog</li><li>Videos</li><li>FAQs</li></ul></div>
</footer>

<div class="bottom-bar">
  <span style="left:74px">© 2020 mervalink.ai. All Rights Reserved.</span>
  <span style="left:917px">Privacy Policy</span>
  <span style="left:1020px">Terms of Service</span>
</div>

</body>
</html>
```